Travel Company is looking for a STAND OUT Business Card

I need a unique Business Card that will truly stand out. Nothing too busy. Simple is good, right? Not looking for a standard design either. No cookie cutter layout. We are a Travel Company that works more with Companies than Travelers. I had an idea to focus and emphasis on the 2 logo a bit more. This is not necessary, however thought it would look interesting. I am just looking for something interesting and a bit different. Does't have to completely off the wall crazy, just not your run of the mill business card.

Target Market(s)

Hoteliers, Resort Management, Call Centers, Executives, Travelers, Families, Businesses

Industry/Entity Type

Hospitality

Contact Information for Business Card

President/CEO - Marco T Villena (title not necessary if design doesn't allow for it)
contact - (407) 555-0182
email - mvillena@roam4ward.example
address - 4127 Brindle Oak Way #164
Orlando, FL 32899
website - www.roam4ward.example

Font styles to use
Serif
Other font styles liked:
• Avenir Next LT Pro BOLD

Requirements
Must have
• simple look and design. Unique design
Nice to have
• I attached the 2 logo separate from the main logo. This can be used separately from the Main Logo, together with the main logo or as main logo. I included the logo font. Use it or not, designers choice.
Should not have
• cookie cutter design. Little use of red other than the logo

```html
<!DOCTYPE html>
<html lang="en">
<head>
<meta charset="utf-8">
<title>roam4ward business card</title>
<link href="https://fonts.googleapis.com/css2?family=Libre+Baskerville:wght@400;700&display=swap" rel="stylesheet">
<style>
  :root {
    --stage: #3a3a3a;
    --ink: #111111;
    --panel: #161616;
    --paper: #ffffff;
    --brand-red: #e8141c;
    --type-light: #ffffff;
    --type-soft: #d9d9d9;
  }
  * { box-sizing: border-box; margin: 0; padding: 0; }
  html, body { width: 1200px; height: 950px; overflow: hidden; }
  body {
    background: var(--stage);
    font-family: "Libre Baskerville", Georgia, serif;
    display: flex;
    flex-direction: column;
    align-items: center;
    justify-content: center;
    gap: 34px;
  }
  .card {
    position: relative;
    width: 760px;
    height: 434px;
    overflow: hidden;
    box-shadow: 0 12px 30px rgba(0,0,0,.45);
  }
  .card--front { background: var(--ink); }
  .card--back { background: var(--paper); }

  .wordmark {
    position: absolute;
    display: flex;
    align-items: center;
    gap: 12px;
    font-family: "Libre Baskerville", Georgia, serif;
    font-weight: 700;
    white-space: nowrap;
  }
  .wordmark__dot {
    width: 18px; height: 18px;
    border-radius: 50%;
    background: var(--brand-red);
    flex: none;
  }
  .card--front .wordmark {
    left: 50%; top: 50%;
    transform: translate(-50%, -50%);
    font-size: 56px;
    color: var(--type-light);
  }
  .card--back .wordmark {
    left: 40px; top: 186px;
    font-size: 40px;
    color: var(--ink);
  }

  .sweep { position: absolute; inset: 0; }
  .sweep .edge-red { fill: var(--brand-red); }
  .sweep .edge-light { fill: var(--paper); }
  .sweep .panel { fill: var(--panel); }

  .contact {
    position: absolute;
    right: 30px;
    top: 92px;
    text-align: right;
    color: var(--type-light);
    font-size: 15px;
    line-height: 1.6;
  }
  .contact__name { font-weight: 700; font-size: 20px; }
  .contact__title { margin-bottom: 12px; color: var(--type-soft); font-style: normal; }
  .contact__address { margin-bottom: 12px; }
  .contact__line {
    display: flex;
    justify-content: flex-end;
    align-items: center;
    gap: 10px;
    white-space: nowrap;
  }
  .contact__line--plain { padding-right: 26px; }
  .icon { width: 16px; height: 16px; fill: var(--brand-red); flex: none; }
</style>
</head>
<body>

  <section class="card card--front" aria-label="Card front">
    <div class="wordmark"><span>roam4ward</span><span class="wordmark__dot"></span></div>
  </section>

  <section class="card card--back" aria-label="Card back">
    <svg class="sweep" viewBox="0 0 760 434" aria-hidden="true">
      <path class="edge-red" d="M360,0 C428,120 432,300 388,434 L760,434 L760,0 Z"/>
      <path class="edge-light" d="M366,0 C434,120 438,300 394,434 L760,434 L760,0 Z"/>
      <path class="panel" d="M374,0 C442,120 446,300 402,434 L760,434 L760,0 Z"/>
    </svg>

    <div class="wordmark"><span>roam4ward</span><span class="wordmark__dot"></span></div>

    <div class="contact">
      <p class="contact__name contact__line--plain">Marco T Villena</p>
      <p class="contact__title contact__line--plain">President/CEO</p>
      <div class="contact__address">
        <p class="contact__line">4127 Brindle Oak Way #164
          <svg class="icon" viewBox="0 0 24 24"><path d="M12 2a7 7 0 0 0-7 7c0 5 7 13 7 13s7-8 7-13a7 7 0 0 0-7-7zm0 9.5A2.5 2.5 0 1 1 12 6.5a2.5 2.5 0 0 1 0 5z"/></svg>
        </p>
        <p class="contact__line contact__line--plain">Orlando, FL 32899</p>
      </div>
      <p class="contact__line">(407) 555-0182
        <svg class="icon" viewBox="0 0 24 24"><path d="M6.6 10.8a15 15 0 0 0 6.6 6.6l2.2-2.2a1 1 0 0 1 1-.25 11.4 11.4 0 0 0 3.6.57 1 1 0 0 1 1 1V20a1 1 0 0 1-1 1A17 17 0 0 1 3 4a1 1 0 0 1 1-1h3.5a1 1 0 0 1 1 1c0 1.25.2 2.45.57 3.6a1 1 0 0 1-.25 1z"/></svg>
      </p>
      <p class="contact__line">mvillena@roam4ward.example
        <svg class="icon" viewBox="0 0 24 24"><path d="M3 5h18v14H3zm2 2v.5l7 4.5 7-4.5V7zm0 3v7h14v-7l-7 4.5z"/></svg>
      </p>
      <p class="contact__line">www.roam4ward.example
        <svg class="icon" viewBox="0 0 24 24"><path d="M12 2a10 10 0 1 0 0 20 10 10 0 0 0 0-20zm6.9 9h-3a15 15 0 0 0-1.3-5.6A8 8 0 0 1 18.9 11zM12 4.1c.9 1.2 1.8 3.5 1.9 6.9h-3.8c.1-3.4 1-5.7 1.9-6.9zM9.4 5.4A15 15 0 0 0 8.1 11h-3a8 8 0 0 1 4.3-5.6zM5.1 13h3a15 15 0 0 0 1.3 5.6A8 8 0 0 1 5.1 13zm6.9 6.9c-.9-1.2-1.8-3.5-1.9-6.9h3.8c-.1 3.4-1 5.7-1.9 6.9zm2.6-1.3a15 15 0 0 0 1.3-5.6h3a8 8 0 0 1-4.3 5.6z"/></svg>
      </p>
    </div>
  </section>

</body>
</html>
```